QuorvaLedgerly.com facebook design

I need 2 designs, one in english and one in spanish for a new investment company called QuorvaLedgerly.com
We invest daily & send text alerts telling people what investments we make so our clients can copy our trades and earn money.
8 out of 10 trades we make go up 20% on the same day!
you can take a look on our facebook page to get ideas.

Target Market(s)

USa-Hispanics bilingual

Industry/Entity Type

Investment

Font styles to use
Sans Serif

Colors

Designer to choose colors to be used in the design.

Requirements
Must have
• see some of our posts on facebook and Let the designer choose.
Nice to have
Should not have

```html
<!DOCTYPE html>
<html lang="en">
<head>
<meta charset="utf-8">
<title>QuorvaLedgerly.com – Facebook Cover</title>
<link rel="stylesheet" href="https://fonts.googleapis.com/css2?family=Montserrat:ital,wght@0,500;0,600;0,700;0,800;1,600&family=Cinzel:wght@400&display=swap">
<style>
  :root {
    --page-bg: #ffffff;
    --navy-deep: #070f24;
    --navy-mid: #0c2350;
    --navy-glow: #12316e;
    --neon: #e3ff1c;
    --gold: #f4c20d;
    --white: #ffffff;
    --muted: #c9d2e6;
    --product-dark: #0a0f2a;
    --product-blue: #2a3fd6;
  }
  * { margin: 0; padding: 0; box-sizing: border-box; }
  html, body {
    width: 1200px; height: 1200px; overflow: hidden;
    background: var(--page-bg);
    font-family: "Montserrat", sans-serif;
  }
  .cover {
    position: absolute; left: 0; top: 345px;
    width: 1200px; height: 510px;
    overflow: hidden;
    background: var(--page-bg);
  }
  .cover__panel { position: absolute; inset: 0; }
  .cover__frame { position: absolute; inset: 0; }

  .brand {
    position: absolute; left: 44px; top: 40px;
    display: flex; align-items: center; gap: 20px;
  }
  .brand__dot {
    width: 100px; height: 100px; border-radius: 50%;
    background: var(--gold);
  }
  .brand__name {
    font-weight: 800; font-size: 26px; color: var(--gold);
    letter-spacing: 0.3px; text-transform: uppercase;
  }
  .brand__slashes {
    font-weight: 600; font-size: 22px; color: var(--white);
    margin-left: -4px; letter-spacing: -2px;
  }

  .headline__kicker {
    position: absolute; left: 178px; top: 150px;
    font-weight: 800; font-size: 34px; line-height: 1.1; color: var(--white);
    letter-spacing: 0;
  }
  .headline__main {
    position: absolute; left: 176px; top: 194px;
    font-weight: 800; font-size: 77px; line-height: 1;
    color: var(--white); letter-spacing: 0.3px;
  }
  .headline__quote {
    position: absolute; left: 180px; top: 278px;
    width: 464px; text-align: center;
    font-weight: 600; font-size: 15.5px; color: var(--white);
  }
  .headline__quote b { font-weight: 800; font-size: 18px; }

  .author {
    position: absolute; left: 178px; top: 312px; width: 466px;
    display: flex; align-items: center; gap: 18px;
  }
  .author__rule { flex: 1; height: 1px; background: var(--muted); }
  .author__name {
    font-family: "Cinzel", serif; font-size: 15px;
    color: var(--white); letter-spacing: 5px;
  }

  .offer {
    position: absolute; left: 106px; top: 392px;
    font-weight: 700; font-size: 14px; color: var(--white);
    letter-spacing: 6.4px; text-transform: uppercase;
  }
  .contact {
    position: absolute; left: 0; top: 430px;
    display: flex; align-items: center; gap: 16px;
  }
  .contact__hatch { width: 500px; height: 24px; }
  .contact__phone {
    font-weight: 800; font-size: 33px; color: var(--white);
    letter-spacing: 0.5px;
  }

  .product {
    position: absolute; left: 770px; top: 34px;
    width: 400px; height: 420px;
  }
</style>
</head>
<body>
  <main class="cover">
    <svg class="cover__panel" width="1200" height="510" viewBox="0 0 1200 510" aria-hidden="true">
      <defs>
        <linearGradient id="panelFill" x1="0" y1="0" x2="1" y2="1">
          <stop offset="0" stop-color="#0a1a3e"/>
          <stop offset="0.55" stop-color="#081530"/>
          <stop offset="1" stop-color="#060d20"/>
        </linearGradient>
      </defs>
      <polygon points="0,0 696,0 822,510 0,510" fill="url(#panelFill)"/>
      <polygon points="0,0 330,0 90,510 0,510" fill="#0d2658" opacity="0.45"/>
    </svg>

    <svg class="cover__frame" width="1200" height="510" viewBox="0 0 1200 510" aria-hidden="true">
      <g fill="none" stroke="var(--neon)" stroke-width="9">
        <polyline points="330,124 1096,124 1096,356 108,356 108,190"/>
      </g>
      <g stroke="var(--white)" stroke-width="4">
        <line x1="484" y1="160" x2="666" y2="160"/>
        <line x1="484" y1="173" x2="666" y2="173"/>
        <line x1="484" y1="186" x2="640" y2="186"/>
      </g>
      <line x1="180" y1="303" x2="644" y2="303" stroke="var(--white)" stroke-width="1"/>
    </svg>

    <div class="brand">
      <span class="brand__dot"></span>
      <span class="brand__name">QuorvaLedgerly.com</span>
      <span class="brand__slashes">///</span>
    </div>

    <h2 class="headline__kicker">STOCK MARKET</h2>
    <h1 class="headline__main">MADE EASY</h1>
    <p class="headline__quote">“<b>8</b> out of 10 my trades profit over <b>20</b> % on the Same Day.”</p>

    <div class="author">
      <span class="author__rule"></span>
      <span class="author__name">TEODOR VALCÁRCEL</span>
      <span class="author__rule"></span>
    </div>

    <p class="offer">Follow my trades live or learn my strategy</p>

    <div class="contact">
      <svg class="contact__hatch" viewBox="0 0 500 24" aria-hidden="true">
        <defs>
          <pattern id="hatch" width="9" height="24" patternUnits="userSpaceOnUse">
            <line x1="2" y1="24" x2="8" y2="0" stroke="var(--white)" stroke-width="1.6"/>
          </pattern>
        </defs>
        <rect width="500" height="24" fill="url(#hatch)"/>
      </svg>
      <span class="contact__phone">305-555-0148</span>
    </div>

    <svg class="product" viewBox="0 0 400 420" role="img" aria-label="Product image: strategy book and companion disc with the author's portrait">
      <defs>
        <linearGradient id="productFill" x1="0" y1="0" x2="0" y2="1">
          <stop offset="0" stop-color="#1a2150"/>
          <stop offset="0.45" stop-color="var(--product-blue)"/>
          <stop offset="1" stop-color="var(--product-dark)"/>
        </linearGradient>
      </defs>
      <polygon points="20,30 250,8 250,380 20,396" fill="url(#productFill)"/>
      <rect x="130" y="200" width="180" height="180" fill="#121a45"/>
      <circle cx="312" cy="292" r="78" fill="#d9dde6"/>
    </svg>
  </main>
</body>
</html>
```